Bright and beautiful business card for a coach

I'm a personal and business coach based in Perth, Australia. I need a business card that whilst subtle and elegant, will stand out and appeal on a table full of cards.

My business name is Tide Mentoring and the business card must represent the warmth and brightness implied in the name, without being gimmicky. It must have a warmth and appeal and be easy to read.

I prefer clean, minimalist designs.

It must align with the feel of my website and socials: https://www.tidementoring.com.au/
https://www.instagram.com/tidementoringau/
https://www.facebook.com/tidementoringau
Updates

Hi Designers Thank you so much for taking the time to submit designs. I wonder if I could have explained myself a little better. Most of the designs that have been submitted look rather formal and many have quite corporate looking embellishments on them (to my eye). I would like softer, warmer, more organic. I’m open to people playing about and being more abstract, using softer embellishments (e.g the line drawing flowers and grasses I’ve used in my socials) incorporating other colours from my palette or like the social icons in my email signature (in PDF), perhaps playing with size/oversize, playing with the bleed. Please don’t be constrained by what I’ve already done, it merely needs to compliment. I’m sorry if I’m not using the right words or have led you astray. I’m no designer, but I’ve done my website, socials, email signature etc all myself (my logo was a design contest) and I was really hoping for my business card to be something more creative than I could have made with a template. Reminder: No black cards/sides please. Thank you 😊

Target Market(s)

Individuals, most likely but not all female. Creative thinkers. Likely professionals.

Industry/Entity Type

Business & Personal Coach

Contact Information for Business Card

(Tide Mentoring Logo) Name: Maren Delsby; Title: Business & Personal Coach; Phone number: +61 (0)438 915307; Email: maren@tidementoring.com.au; Website: https://tidementoring.com.au; Social icons for Facebook, Instagram & LinkedIn: @tidementoringAU. Optional strapline: "A thinking partner to help you cut through the noise"

Font styles to use
Sans Serif

Colors
00AB8E
00BBA5
67D7C9
C6EFE9
E9F9F6
59FF00
82FF00
B8FF75
E3FFCB
F4FFEA
FFC000
F8CF3A
FAE287
FDF2CF
FEFAEE

Requirements
Must have
• Must align with feel of my website and socials. Must have a pop of #FFC000 (possibly whole of one side, or at least a block). Bright or white background. Easy to read.
Nice to have
• Possibly incorporate the sunshine/grass picture I have used in website and socials - will upload.
Should not have
• Must not be black or dark. Not impersonal or corporate looking.

```html
<!DOCTYPE html>
<html lang="en">
<head>
<meta charset="utf-8">
<title>Tide Mentoring – Business Card</title>
<link rel="stylesheet" href="https://fonts.googleapis.com/css2?family=Lato:wght@400;700;900&display=swap">
<style>
  :root {
    --backdrop: #5d5d5b;
    --card: #ffffff;
    --sun: #ffc000;
    --sun-soft: #fcd86a;
    --ink: #161616;
    --icon-grey: #5f6c6c;
    --social-fb: #c97a1c;
    --social-ig: #cfc84a;
    --social-in: #ffc000;
    --grass-dark: #2f7a1a;
    --grass-mid: #5fa02c;
    --grass-light: #c6db86;
  }
  * { margin: 0; padding: 0; box-sizing: border-box; }
  html, body { width: 1200px; height: 1200px; overflow: hidden; }
  body { background: var(--backdrop); font-family: "Lato", sans-serif; position: relative; }

  .card {
    position: absolute; left: 183px; width: 831px; height: 462px;
    background: var(--card); overflow: hidden;
  }
  .card--front { top: 104px; }
  .card--back { top: 628px; }
  .card__art { position: absolute; inset: 0; width: 100%; height: 100%; }

  .strapline {
    position: absolute; left: 0; right: 0; bottom: 0; height: 25px;
    background: rgba(255,255,255,0.28);
    display: flex; align-items: center; justify-content: center;
    font-size: 11px; font-weight: 900; letter-spacing: 0.26em;
    text-transform: uppercase; color: var(--ink);
  }

  .brand-name {
    position: absolute; color: var(--sun); font-weight: 400;
    letter-spacing: 0.04em; white-space: nowrap;
  }
  .card--front .brand-name { left: 150px; top: 88px; font-size: 48px; }
  .card--back .brand-name { left: 500px; top: 118px; font-size: 36px; }

  .contact { position: absolute; left: 78px; top: 50px; }
  .contact__name {
    display: inline-block; color: var(--sun); font-size: 28px; font-weight: 700;
    letter-spacing: 0.12em; text-transform: uppercase; line-height: 1;
    padding: 0 4px 2px 6px; border-bottom: 2px solid var(--sun);
  }
  .contact__title { margin: 10px 0 0 9px; font-size: 20px; color: var(--ink); }
  .contact__list { list-style: none; margin: 10px 0 0 9px; }
  .contact__item {
    display: flex; align-items: center; height: 31px;
    font-size: 16px; color: var(--ink);
  }
  .contact__icon {
    width: 22px; height: 22px; border-radius: 50%; background: var(--icon-grey);
    display: flex; align-items: center; justify-content: center; margin-right: 10px;
  }
  .contact__icon svg { width: 13px; height: 13px; }
  .social-dot { width: 22px; height: 22px; border-radius: 50%; margin-right: 8px; }
  .social-dot--fb { background: var(--social-fb); }
  .social-dot--ig { background: var(--social-ig); }
  .social-dot--in { background: var(--social-in); margin-right: 10px; }
</style>
</head>
<body>

<section class="card card--front">
  <svg class="card__art" viewBox="0 0 1337 743" preserveAspectRatio="none">
    <defs>
      <radialGradient id="grassFront" cx="0.55" cy="0.15" r="0.9">
        <stop offset="0" stop-color="var(--grass-light)"/>
        <stop offset="0.45" stop-color="var(--grass-mid)"/>
        <stop offset="1" stop-color="var(--grass-dark)"/>
      </radialGradient>
    </defs>
    <path class="wave-soft" fill="var(--sun-soft)" d="M0,225 C300,320 550,350 800,300 C1000,262 1150,240 1337,255 L1337,295 C1150,265 1000,275 800,328 C550,378 300,340 0,298 Z"/>
    <path class="wave-sun" fill="var(--sun)" d="M0,215 C300,310 550,335 800,285 C1000,245 1150,170 1337,205 L1337,285 C1150,255 1000,262 800,316 C550,368 300,328 0,288 Z"/>
    <path class="photo-area" role="img" aria-label="Photo of dewy green grass in soft sunlight" fill="url(#grassFront)" d="M0,318 C300,362 550,388 800,336 C1000,296 1150,268 1337,302 L1337,743 L0,743 Z"/>
  </svg>
  <span class="brand-name">Tide Mentoring</span>
  <p class="strapline">A thinking partner to help you cut through the noise</p>
</section>

<section class="card card--back">
  <svg class="card__art" viewBox="0 0 1337 743" preserveAspectRatio="none">
    <defs>
      <radialGradient id="grassBack" cx="0.55" cy="0.1" r="0.9">
        <stop offset="0" stop-color="var(--grass-light)"/>
        <stop offset="0.5" stop-color="var(--grass-mid)"/>
        <stop offset="1" stop-color="var(--grass-dark)"/>
      </radialGradient>
    </defs>
    <path class="wave-soft" fill="var(--sun-soft)" d="M0,405 C300,495 550,520 800,465 C1000,420 1150,370 1337,395 L1337,420 C1150,395 1000,420 800,480 C550,540 300,525 0,430 Z"/>
    <path class="wave-sun" fill="var(--sun)" d="M0,430 C300,510 550,530 800,480 C1000,440 1150,395 1337,410 L1337,495 C1150,470 1000,480 800,520 C550,575 300,560 0,500 Z"/>
    <path class="wave-soft" fill="var(--sun-soft)" d="M0,500 C300,560 550,575 800,520 C1000,480 1150,470 1337,495 L1337,503 C1150,480 1000,490 800,532 C550,588 300,575 0,512 Z"/>
    <path class="photo-area" role="img" aria-label="Photo of dewy green grass in soft sunlight" fill="url(#grassBack)" d="M0,525 C300,585 550,600 800,548 C1000,505 1150,480 1337,512 L1337,743 L0,743 Z"/>
  </svg>

  <div class="contact">
    <h1 class="contact__name">Maren Delsby</h1>
    <p class="contact__title">Business &amp; Personal Coach</p>
    <ul class="contact__list">
      <li class="contact__item">
        <span class="contact__icon"><svg viewBox="0 0 24 24"><path fill="#fff" d="M6.6 10.8a15 15 0 0 0 6.6 6.6l2.2-2.2a1 1 0 0 1 1-.25 11.4 11.4 0 0 0 3.6.57 1 1 0 0 1 1 1V20a1 1 0 0 1-1 1A17 17 0 0 1 3 4a1 1 0 0 1 1-1h3.5a1 1 0 0 1 1 1c0 1.25.2 2.45.57 3.57a1 1 0 0 1-.25 1z"/></svg></span>
        +61 (0)438 915307
      </li>
      <li class="contact__item">
        <span class="contact__icon"><svg viewBox="0 0 24 24"><rect x="3" y="6" width="18" height="12" rx="1.5" fill="none" stroke="#fff" stroke-width="2"/><path d="M3.5 7l8.5 6 8.5-6" fill="none" stroke="#fff" stroke-width="2"/></svg></span>
        maren@tidementoring.com.au
      </li>
      <li class="contact__item">
        <span class="contact__icon"><svg viewBox="0 0 24 24" fill="none" stroke="#fff" stroke-width="1.6"><circle cx="12" cy="12" r="9"/><ellipse cx="12" cy="12" rx="4" ry="9"/><path d="M3 12h18M5 7h14M5 17h14"/></svg></span>
        https://tidementoring.com.au
      </li>
      <li class="contact__item">
        <span class="social-dot social-dot--fb" aria-hidden="true"></span>
        <span class="social-dot social-dot--ig" aria-hidden="true"></span>
        <span class="social-dot social-dot--in" aria-hidden="true"></span>
        @tidementoringAU
      </li>
    </ul>
  </div>

  <span class="brand-name">Tide Mentoring</span>
  <p class="strapline">A thinking partner to help you cut through the noise</p>
</section>

</body>
</html>
```